Real Estate 2015 sold listings postcard

Real estate. I want one side to list 2015 sales. Mailing side with additional information. I am including a "concept" but it needs to be professionalized... Feel free to change color, fonts, layout, add watermark, whatever you think will work. Text on backside may be tweaked. I do want postcards addressed. How do i send mailing list or does Brightmark Press do that part?

NOTE: Postcard should be 8.5 x 5.5 inches.
Updates

postcard should be 8.5" x 5.5" size

Target Market(s)

Home owners who may want to sell

Industry/Entity Type

Real Estate Agent

Requirements
Must have
• The sold information and contact oinformation I have provided
Nice to have
• Watermark with my initials

```html
<!DOCTYPE html>
<html lang="en">
<head>
<meta charset="utf-8">
<title>2015 Sold Listings Postcard</title>
<link href="https://fonts.googleapis.com/css2?family=Lato:wght@400;700;900&family=Roboto+Condensed:wght@400;700&display=swap" rel="stylesheet">
<style>
:root{
  --gold:#e9a51d;
  --ink:#141414;
  --paper:#ffffff;
  --backdrop:#e8e5e1;
  --muted:#333;
}
*{box-sizing:border-box;margin:0;padding:0}
html,body{width:900px;height:1200px;overflow:hidden}
body{background:var(--backdrop);position:relative;font-family:'Lato',sans-serif;color:var(--ink)}
.card{position:absolute;background:var(--paper);overflow:hidden}
.front{left:90px;top:95px;width:722px;height:465px}
.back{left:95px;top:650px;width:710px;height:460px}

.portrait{position:absolute;border:2px solid var(--gold);background:linear-gradient(160deg,#8a6a55,#b8412f 70%,#c9c3bd)}
.front .portrait{left:8px;top:13px;width:69px;height:88px}
.agent-name{position:absolute;font-family:'Roboto Condensed',sans-serif;font-weight:700;line-height:1}
.front .agent-name{left:85px;top:16px;font-size:20px}
.agent-role{position:absolute;font-family:'Roboto Condensed',sans-serif;font-weight:700;font-size:13px}
.front .agent-role{left:85px;top:38px}
.agent-license{position:absolute;font-family:'Roboto Condensed',sans-serif;font-weight:700;font-size:10px}
.front .agent-license{left:85px;top:56px}

.top-notch{position:absolute;left:265px;top:0;width:210px;height:50px}
.brokerage{position:absolute;right:24px;top:42px;font-family:'Lato',sans-serif;font-weight:700;font-size:17px;letter-spacing:1.5px;display:flex;align-items:center;gap:7px}
.brokerage .mark{width:12px;height:12px;background:var(--gold)}
.sales-title{position:absolute;left:0;right:0;top:72px;text-align:center;padding-left:45px;font-weight:900;font-size:20px;color:var(--gold);letter-spacing:.2px}
.sold-rule{position:absolute;left:0;right:0;top:106px;height:4px;background:var(--ink)}
.sold-label{position:absolute;left:306px;top:97px;width:80px;background:var(--paper);text-align:center;font-size:19px;font-weight:400;line-height:22px}
.realtors-tag{position:absolute;right:0;top:103px;width:145px;height:9px;background:var(--ink);color:#fff;font-size:7px;line-height:9px;padding-left:32px;letter-spacing:.5px}

.sales-table{position:absolute;left:26px;top:125px;font-size:12px;line-height:15.1px}
.sales-table .row{display:grid;grid-template-columns:96px 52px 60px 88px 82px 88px 90px 62px 60px;white-space:nowrap}
.sales-table .head{margin-bottom:1px}
.sales-table .c{text-align:center}
.sales-table .r{text-align:right}
.sales-table .l{text-align:left}
.sales-table .head .r,.sales-table .head .l{text-align:left}
.sales-table .sq{padding-right:-4px}

.contact-bar{position:absolute;left:0;right:0;top:390px;height:35px;background:var(--ink);color:#fff;display:flex;align-items:center;font-size:16px}
.contact-item{display:flex;align-items:center;gap:10px;position:absolute}
.contact-item svg{flex:none}
.disclaimer-bar{position:absolute;left:0;right:0;top:425px;height:40px;background:var(--gold);text-align:center;font-size:12.5px;line-height:40px;color:var(--ink)}

.back .portrait{left:20px;top:17px;width:65px;height:83px}
.back .agent-name{left:94px;top:21px;font-size:16px}
.back .agent-role{left:94px;top:37px;font-size:11px}
.back .agent-license{left:94px;top:53px;font-size:9px}
.back-email{position:absolute;left:94px;top:63px;font-family:'Roboto Condensed',sans-serif;font-weight:700;font-size:14px}
.back-phone{position:absolute;left:94px;top:77px;font-family:'Roboto Condensed',sans-serif;font-weight:700;font-size:20px}
.chevron{position:absolute;left:0;top:0}
.season-kicker{position:absolute;left:20px;top:114px;font-family:'Roboto Condensed',sans-serif;font-weight:700;font-size:11px}
.season-head{position:absolute;left:20px;top:129px;font-family:'Roboto Condensed',sans-serif;font-weight:700;font-size:18px}
.perks{position:absolute;left:20px;top:152px;list-style:none;font-weight:700;font-size:13px;line-height:17px}
.perks li{display:flex;align-items:center;gap:5px}
.perks li::before{content:"";width:7px;height:7px;background:var(--gold)}
.reach{position:absolute;left:22px;top:198px;font-size:13px}
.cta{position:absolute;left:22px;top:216px;font-family:'Roboto Condensed',sans-serif;font-weight:700;font-size:15.5px}
.pitch{position:absolute;left:20px;top:256px;width:280px;font-size:8.6px;line-height:11.4px;text-align:justify;color:var(--muted)}
.pitch p+p{margin-top:11px}
.back-footer{position:absolute;left:0;top:432px;width:292px;height:28px;background:var(--ink)}
.stamp-box{position:absolute;left:598px;top:38px;width:65px;height:64px;border:1.5px solid var(--ink)}
.address-line{position:absolute;left:416px;width:234px;height:2px;background:var(--ink)}
</style>
</head>
<body>

<section class="card front" aria-label="Front: 2015 sales in your neighborhood">
  <svg class="top-notch" viewBox="0 0 210 50" aria-hidden="true"><polygon points="0,0 210,0 105,50" fill="var(--gold)"/></svg>
  <div class="portrait" role="img" aria-label="Portrait photo of agent Dana Whitfield"></div>
  <div class="agent-name">Dana Whitfield</div>
  <div class="agent-role">Relocation Specialist</div>
  <div class="agent-license">California License 01234567</div>
  <div class="brokerage"><span class="mark"></span>HARBOR CREST</div>
  <h1 class="sales-title">2015 SALES IN YOUR NEIGHBORHOOD</h1>
  <div class="sold-rule"></div>
  <div class="sold-label">SOLD</div>
  <div class="realtors-tag">REALTORS</div>

  <div class="sales-table">
    <div class="row head"><span>Address</span><span class="l" style="padding-left:26px">BR</span><span class="l" style="padding-left:20px">BA</span><span class="l" style="padding-left:2px">Sq Ft</span><span class="l" style="padding-left:-6px">Lot Size</span><span class="l" style="padding-left:20px">List Price</span><span class="l" style="padding-left:18px">Sale Price</span><span class="l" style="padding-left:22px">$/Sq. Ft</span><span class="l" style="padding-left:14px">DOM</span></div>
    <div class="row"><span>387 Elm PL*</span><span class="c">3</span><span class="c">3 1/2</span><span class="r">2588</span><span class="r">9239</span><span class="c">3088000</span><span class="c">3,100,000</span><span class="c">1198</span><span class="c">9</span></div>
    <div class="row"><span>3657 Briar ST</span><span class="c">4</span><span class="c">3</span><span class="r">2228</span><span class="r">6147</span><span class="c">2998000</span><span class="c">3000000</span><span class="c">1346</span><span class="c">23</span></div>
    <div class="row"><span>261 Brookview DR</span><span class="c">4</span><span class="c">3</span><span class="r">2185</span><span class="r">7040</span><span class="c">2500000</span><span class="c">2925000</span><span class="c">1,339</span><span class="c">9</span></div>
    <div class="row"><span>437 Fenwick AVE*</span><span class="c">4</span><span class="c">2</span><span class="r">1611</span><span class="r">13,237</span><span class="c">2498000</span><span class="c">2610000</span><span class="c">1620</span><span class="c">8</span></div>
    <div class="row"><span>4123 Dover AVE*</span><span class="c">4</span><span class="c">2</span><span class="r">2227</span><span class="r">8700</span><span class="c">2295000</span><span class="c">2595000</span><span class="c">1165</span><span class="c">8</span></div>
    <div class="row"><span>76 Rosewood CIR *</span><span class="c">3</span><span class="c">2</span><span class="r">1364</span><span class="r">5917</span><span class="c">1788000</span><span class="c">2525000</span><span class="c">1851</span><span class="c">8</span></div>
    <div class="row"><span>3665 Redwood CIR</span><span class="c">4</span><span class="c">2</span><span class="r">1646</span><span class="r">6404</span><span class="c">2500000</span><span class="c">2475000</span><span class="c">1504</span><span class="c">18</span></div>
    <div class="row"><span>410 Aspen PL*</span><span class="c">3</span><span class="c">2</span><span class="r">1674</span><span class="r">11200</span><span class="c">2498000</span><span class="c">2450000</span><span class="c">1464</span><span class="c">16</span></div>
    <div class="row"><span>291 Brookview DR*</span><span class="c">4</span><span class="c">2</span><span class="r">1690</span><span class="r">8178</span><span class="c">2199000</span><span class="c">2400000</span><span class="c">1420</span><span class="c">7</span></div>
    <div class="row"><span>303 Brookview DR.</span><span class="c">3</span><span class="c">2</span><span class="r">1674</span><span class="r">8538</span><span class="c">2200000</span><span class="c">2260000</span><span class="c">1350</span><span class="c">97</span></div>
    <div class="row"><span>93 Rosewood CIR</span><span class="c">3</span><span class="c">2</span><span class="r">1243</span><span class="r">6080</span><span class="c">1488000</span><span class="c">2250000</span><span class="c">1810</span><span class="c">7</span></div>
    <div class="row"><span>3702 Carver CIR *</span><span class="c">4</span><span class="c">2</span><span class="r">1333</span><span class="r">6493</span><span class="c">1895000</span><span class="c">2227500</span><span class="c">1671</span><span class="c">6</span></div>
    <div class="row"><span>372 Parkview DR *</span><span class="c">3</span><span class="c">2</span><span class="r">1740</span><span class="r">6324</span><span class="c">2200000</span><span class="c">2180000</span><span class="c">1,253</span><span class="c">12</span></div>
    <div class="row"><span>3647 Briar ST</span><span class="c">4</span><span class="c">2</span><span class="r">1474</span><span class="r">6111</span><span class="c">1799900</span><span class="c">2115000</span><span class="c">1,435</span><span class="c">17</span></div>
    <div class="row"><span>60 Rosewood Cir</span><span class="c">4</span><span class="c">2</span><span class="r">1456</span><span class="r">6111</span><span class="c">1788000</span><span class="c">200000</span><span class="c">1374</span><span class="c">11</span></div>
    <div class="row"><span>252 Fairview CT</span><span class="c">3</span><span class="c">2</span><span class="r">1428</span><span class="r">10,624</span><span class="c">1,950,000</span><span class="c">2,100,000</span><span class="c">1471</span><span class="c">20</span></div>
  </div>

  <div class="contact-bar">
    <div class="contact-item" style="left:33px">
      <svg width="20" height="13" viewBox="0 0 20 13" aria-hidden="true"><rect width="20" height="13" rx="1" fill="var(--gold)"/><polyline points="1,1 10,8 19,1" fill="none" stroke="var(--ink)" stroke-width="1.4"/></svg>
      <span>dwhitfield@hcrealty.com</span>
    </div>
    <div class="contact-item" style="left:285px">
      <svg width="14" height="15" viewBox="0 0 14 15" aria-hidden="true"><rect width="14" height="15" rx="2" fill="var(--gold)"/><path d="M4 3c-1 1-1 3 1 6s4 4 5 3l1-1-2-2-1 1c-1-.5-2-2-2.5-3l1-1-1.5-2z" fill="var(--ink)"/></svg>
      <span>650-555-0162</span>
    </div>
    <div class="contact-item" style="left:510px">
      <svg width="18" height="14" viewBox="0 0 18 14" aria-hidden="true"><ellipse cx="9" cy="7" rx="8" ry="6.5" fill="var(--gold)"/><ellipse cx="9" cy="7" rx="3.5" ry="6.5" fill="none" stroke="var(--ink)" stroke-width="1"/><line x1="1" y1="7" x2="17" y2="7" stroke="var(--ink)" stroke-width="1"/></svg>
      <span>www.dwhitfield.com</span>
    </div>
  </div>
  <div class="disclaimer-bar">* indicates Harbor Crest Realtors listing or sale. This information is deemed reliable, but not verified or guaranteed.</div>
</section>

<section class="card back" aria-label="Back: mailing side">
  <svg class="chevron" width="710" height="460" viewBox="0 0 710 460" aria-hidden="true">
    <polygon points="222,10 405,205 305,432 294,432 387,202" fill="var(--gold)"/>
    <polygon points="210,0 224,0 387,202 297,432 284,432 373,202" fill="var(--ink)"/>
  </svg>
  <div class="portrait" role="img" aria-label="Portrait photo of agent Dana Whitfield"></div>
  <div class="agent-name">Dana Whitfield</div>
  <div class="agent-role">Relocation Specialist</div>
  <div class="agent-license">California License 01234567</div>
  <div class="back-email">dwhitfield@hcrealty.com</div>
  <div class="back-phone">650-555-0148</div>

  <div class="season-kicker">TRADITIONALLY, FEB. THROUGH APRIL ARE</div>
  <h2 class="season-head">THE BEST MONTHS TO SELL</h2>
  <ul class="perks"><li>Most Offers</li><li>Highest prices</li></ul>
  <p class="reach">Our Listings are advertised locally and in 40 countries!!</p>
  <p class="cta">Don't Wait. Call Now for a Private Consultation!</p>
  <div class="pitch">
    <p>Our market continues to be strong, which reflects both our vibrant and growing local economy and our seemingly chronic shortage of inventory. As long as those conditions continue, our market values will remain high. That is good news to sellers who may want to down-size or move to a different area for a new job, or maybe to be closer to family.</p>
    <p>I am a Harbor Crest Realtors certified Relocation Specialist, and, as such, I can connect you with experienced and professional real estate agent anywhere in the country and in most countries around the world. We can co-ordinate your transactions at both ends, making your transition as seamless as possible. If you are planning a move, across the street or across the county, call me now for a confidential consultation.</p>
  </div>
  <div class="back-footer"></div>

  <div class="stamp-box" aria-label="Stamp area"></div>
  <div class="address-line" style="top:290px"></div>
  <div class="address-line" style="top:325px"></div>
  <div class="address-line" style="top:366px"></div>
</section>

</body>
</html>
```